brisk-vale.com Real Estate, Investment, Financial corporate

Real Estate, Investment, Financial corporate looking site. Show present a professional firm, with an elegant display. Please see the attached file which includes the logo, palette and fonts.
Updates

We just starting the brief today. ( logo was delayed)

Target Market(s)

Investors, Corporate , B2b

Industry/Entity Type

real-estate investments

Number of Pages Required

3 page

Requirements
Must have
• Dazzling Homepage
Nice to have
• paralex

```html
<!DOCTYPE html>
<html lang="en">
<head>
<meta charset="utf-8">
<title>Brisk-Vale Company</title>
<link href="https://fonts.googleapis.com/css2?family=Arvo:wght@700&family=Montserrat:wght@400;500;600;700&display=swap" rel="stylesheet">
<style>
:root{
  --navy:#030d2b;
  --gold:#c9a85a;
  --light:#f2f2f2;
  --white:#ffffff;
  --ink:#0b1433;
  --rule:#1d2748;
  --blue:#0077be;
}
*{margin:0;padding:0;box-sizing:border-box}
html,body{width:1200px;height:2916px;overflow:hidden;background:var(--navy)}
body{position:relative;font-family:'Montserrat',sans-serif;color:var(--white)}
.abs{position:absolute}
.slab{font-family:'Arvo',serif;font-weight:700}

/* header */
.brand-mark{left:68px;top:34px;width:183px;height:104px;background:linear-gradient(135deg,#1a3f7a,#0d2350 60%,#2a4f8c)}
.brand-name{left:283px;top:26px;font-size:40px;color:var(--gold);letter-spacing:.5px}
.nav{top:103px;left:283px;width:900px;height:24px;font-size:17px}
.nav span{position:absolute;white-space:nowrap}

/* hero */
.slide{left:49px;top:175px;width:700px;height:466px;background:linear-gradient(180deg,#eef0ee 0%,#dcd8cc 45%,#b9a488 100%)}
.arrow{top:387px;width:42px;height:42px;background:rgba(20,20,20,.55);display:flex;align-items:center;justify-content:center}
.dots{top:652px;left:306px;display:flex;gap:9px;align-items:center}
.dots i{display:block;width:12px;height:12px;border-radius:50%;background:#8a8fa0}
.dots i.on{width:14px;height:14px;background:#fff}
.gallery{left:801px;top:175px;width:371px;height:371px;display:grid;grid-template-columns:repeat(3,1fr);grid-template-rows:repeat(3,1fr);gap:3px}
.gallery div{background:linear-gradient(135deg,#e8e4dc,#b9b0a2)}
.gallery .dark{background:linear-gradient(135deg,#3b3d42,#a9a49a)}
.gallery .pool{background:linear-gradient(160deg,#2b6fc4,#e9ecea 55%,#1aa6a6)}

.headline{top:700px;left:0;width:1200px;text-align:center;font-size:40px;line-height:46px;color:var(--white)}
.address{top:808px;left:0;width:1200px;text-align:center;font-size:16px}

.stat{top:889px;width:200px;height:152px;border-top:1px solid var(--rule);border-bottom:1px solid var(--rule);text-align:center}
.stat .label{margin-top:34px;font-size:16px;font-weight:700}
.stat .num{margin-top:16px;font-size:44px;font-weight:700}

/* about */
.about{top:1070px;left:0;width:1200px;height:336px;background:var(--light);color:var(--ink)}
.about h2{position:absolute;left:153px;top:56px;font-size:38px}
.about .pic{position:absolute;left:164px;top:129px;width:266px;height:150px;background:linear-gradient(135deg,#1a3f7a,#0d2350 60%,#2a4f8c)}
.about p{position:absolute;left:472px;top:56px;width:570px;font-size:16px;line-height:28.4px;color:#333}

/* services */
.services{top:1406px;left:0;width:1200px;height:569px;background:linear-gradient(180deg,#e3cf92 0%,#d9c07a 55%,#cdb06a 100%);color:var(--ink);text-align:center}
.services h2{position:absolute;top:107px;left:0;width:1200px;font-size:46px}
.services p{position:absolute;top:188px;left:265px;width:670px;font-size:16px;line-height:28.4px;color:#5a4f3a}
.services .item{position:absolute;top:366px;font-size:28px;font-weight:600;line-height:40px;transform:translateX(-50%);white-space:nowrap}

/* learn */
.learn-title{top:2026px;left:0;width:1200px;text-align:center;font-size:31px}
.card{top:2091px;width:360px;height:239px}
.card.c1{left:28px;background:linear-gradient(160deg,#2d7fd6,#e6e8e4 55%,#3b6e2a)}
.card.c2{left:420px;background:linear-gradient(180deg,#eef0ee,#c8bba4)}
.card.c3{left:812px;background:linear-gradient(135deg,#3a3c40,#c9c6bf)}
.caption{top:2362px;width:360px;text-align:center;font-size:16px}
.learn-copy{top:2421px;left:266px;width:668px;font-size:16px;line-height:28.4px;text-align:justify}

/* contact */
.contact-title{top:2614px;left:0;width:1200px;text-align:center;font-size:32px}
.agent-photo{left:153px;top:2681px;width:277px;height:155px;background:var(--blue)}
.agent{left:461px;top:2683px;width:290px;font-size:16px;line-height:28.4px}
.agent h3{font-size:16px;font-weight:700;margin-bottom:28px}
.team{left:770px;top:2683px;width:320px;font-size:16px;line-height:28.4px}
.team h3{font-size:16px;margin-bottom:22px}
.gold{color:var(--gold)}
</style>
</head>
<body>

<header>
  <div class="abs brand-mark" role="img" aria-label="City skyline brand graphic"></div>
  <div class="abs brand-name slab">BRISK-VALE COMPANY</div>
  <nav class="abs nav">
    <span style="left:0">BRISK-VALE COMPANY</span>
    <span style="left:298px">About Us</span>
    <span style="left:436px">Our Services</span>
    <span style="left:600px">Learn</span>
    <span style="left:710px">Contact Us</span>
  </nav>
</header>

<section class="hero">
  <div class="abs slide" role="img" aria-label="Bright living room with white sofas and black armchairs"></div>
  <div class="abs arrow" style="left:38px"><svg width="14" height="20" viewBox="0 0 14 20"><path d="M10 3 3 10l7 7" fill="none" stroke="#fff" stroke-width="2"/></svg></div>
  <div class="abs arrow" style="left:717px"><svg width="14" height="20" viewBox="0 0 14 20"><path d="M4 3l7 7-7 7" fill="none" stroke="#fff" stroke-width="2"/></svg></div>
  <div class="abs dots"><i class="on"></i><i></i><i></i><i></i><i></i><i></i><i></i><i></i><i></i></div>
  <div class="abs gallery" role="img" aria-label="Gallery of interior and exterior property photos">
    <div></div><div></div><div></div>
    <div></div><div></div><div></div>
    <div class="pool"></div><div class="dark"></div><div></div>
  </div>

  <h1 class="abs headline slab">Pioneer in Real State, Investment, Financial<br>corporate</h1>
  <div class="abs address">123 Any Street, HJ 12345</div>

  <div class="abs stat" style="left:153px"><div class="label">Built Year</div><div class="num">2017</div></div>
  <div class="abs stat" style="left:384px"><div class="label">Investment Funds</div><div class="num">55</div></div>
  <div class="abs stat" style="left:616px"><div class="label">Mortgage Help</div><div class="num">35</div></div>
  <div class="abs stat" style="left:848px"><div class="label">Rentals</div><div class="num">25</div></div>
</section>

<section class="abs about">
  <h2 class="slab">About Us</h2>
  <div class="pic" role="img" aria-label="City skyline graphic on an open hand"></div>
  <p><strong style="color:var(--ink)">Lorem ipsum</strong> dolor sit amet, consectetur adipiscing elit, sed do eiusmod tempor incididunt ut labore et dolore magna aliqua. Ut enim ad minim veniam, quis nostrud exercitation ullamco laboris nisi ut aliquip ex ea commodo consequat. Duis aute irure dolor in reprehenderit in voluptate velit esse cillum dolore eu fugiat nulla pariatur. Excepteur sint occaecat cupidatat non proident, sunt in culpa qui officia deserunt mollit anim id est laborum.</p>
</section>

<section class="abs services" role="img" aria-label="Living room photo beneath a gold tint">
  <h2 class="slab">Our Services</h2>
  <p>Lorem ipsum dolor sit amet, consectetur adipiscing elit, sed do eiusmod tempor incididunt ut labore et dolore magna aliqua. Ut enim ad minim veniam, quis nostrud exercitation ullamco laboris nisi ut aliquip ex ea commodo consequat. Duis aute irure dolor in reprehenderit in voluptate velit esse cillum dolore eu fugiat nulla pariatur.</p>
  <div class="item" style="left:130px">Rentals</div>
  <div class="item" style="left:383px">Mortgage<br>Help</div>
  <div class="item" style="left:600px">Land</div>
  <div class="item" style="left:817px">Investment<br>Funds</div>
  <div class="item" style="left:998px">Rentals</div>
</section>

<section class="learn">
  <h2 class="abs learn-title slab">Learn</h2>
  <div class="abs card c1" role="img" aria-label="Modern white villa with pool"></div>
  <div class="abs card c2" role="img" aria-label="Bright living room interior"></div>
  <div class="abs card c3" role="img" aria-label="Glass-partitioned hallway"></div>
  <div class="abs caption" style="left:28px">Packages</div>
  <div class="abs caption" style="left:420px">Blog</div>
  <div class="abs caption" style="left:812px">How it works</div>
  <p class="abs learn-copy">Lorem ipsum dolor sit amet, consectetur adipiscing elit, sed do eiusmod tempor incididunt ut labore et dolore magna aliqua. Ut enim ad minim veniam, quis nostrud exercitation ullamco laboris nisi ut aliquip ex ea commodo consequat. Duis aute irure dolor in reprehenderit in voluptate velit esse cillum dolore eu fugiat nulla pariatur.</p>
</section>

<section class="contact">
  <h2 class="abs contact-title slab">Contact Us</h2>
  <div class="abs agent-photo" role="img" aria-label="Agent photo placeholder"></div>
  <div class="abs agent">
    <h3>About Agent</h3>
    <p><strong>Lorem ipsum</strong> dolor sit amet, consectetur adipiscing elit, sed do eiusmod tempor incididunt ut labore et dolore magna aliqua. Lorem ipsum dolor sit amet, consectetur adipiscing elit.</p>
  </div>
  <div class="abs team">
    <h3 class="slab">Lorem ipsum Real Estate Team:</h3>
    <div class="gold">example@example.com</div>
    <div class="gold">(123)-456-789</div>
    <div>1 Example Street,</div>
    <div>Anytown, 10100</div>
    <div>USA</div>
  </div>
</section>

</body>
</html>
```